DRUM needs a contemporary simple brochure

We help companies understand their customers, and we would like to send a minimalistic card/brochure to potential clients to introduce our company. The card will be A6 in size (ie A5 folded once) and so will have a front, an inside front, and inside back, and a back page. It can either be portrait or landscape.
It should convey contemporary/modern, bold, fun, uncomplicated/simplicity, be clean/uncluttered, and use friendly and easy to read fonts.
Attached is the information the brochure/card should contain, together with colour palatte and another document which shows our logo, existing stationary etc to give you a feel of the brand. The background of the card could be black, yellow or white (or a combination). thanks, mark
Updates
Hi everyone. Just to let you know that the card will be A6 size, will have a matt laminate finish and can include spot uv. thanks, mark
Reason: Hi, I am looking for some better quality designs so i have extended the deadline and significantly increased the budget. thanks, mark
Target Market(s)
Marketing professionals in large corporates
Industry/Entity Type
It Company
Requirements
Must have
- use our company colours (attached)

```html
<!DOCTYPE html>
<html lang="en">
<head>
<meta charset="utf-8">
<title>DRUM brochure</title>
<link rel="stylesheet" href="https://fonts.googleapis.com/css2?family=Ubuntu:wght@400;500;700&family=Open+Sans:wght@600;700&display=swap">
<style>
  :root{
    --yellow:#fdc800;
    --charcoal:#2f2f2f;
    --chalk:#353535;
    --ink:#3a3a3a;
    --white:#f4f4f4;
    --photo-top:#8f9a92;
    --photo-bottom:#6e7870;
    --backdrop:#e4e4e4;
  }
  *{margin:0;padding:0;box-sizing:border-box}
  html,body{width:1200px;height:1000px;overflow:hidden}
  body{background:var(--backdrop);font-family:'Ubuntu',sans-serif;position:relative}

  .spread{position:absolute;box-shadow:0 6px 18px rgba(0,0,0,.25)}

  /* Cover spread */
  .cover{left:85px;top:25px;width:700px;height:540px;background:var(--yellow)}
  .cover__band{position:absolute;left:0;top:0;width:100%;height:150px;background:var(--charcoal)}
  .cover__fold{position:absolute;left:350px;top:0;width:1px;height:100%;background:rgba(0,0,0,.12)}
  .wordmark{position:absolute;font-family:'Ubuntu',sans-serif;font-weight:500;line-height:1;letter-spacing:1px;text-transform:uppercase;color:var(--ink)}
  .wordmark--back{right:370px;top:290px;font-size:40px}
  .wordmark--front{right:30px;top:170px;font-size:72px}
  .contact{position:absolute;right:370px;top:350px;text-align:right;font-family:'Open Sans',sans-serif;font-weight:600;font-size:10px;line-height:15px;color:var(--ink);font-style:normal}
  .cover__photo{position:absolute;left:365px;top:250px;width:335px;height:200px;background:linear-gradient(160deg,var(--photo-top),var(--photo-bottom))}
  .cover__quote{position:absolute;left:385px;top:322px;width:150px;font-family:'Open Sans',sans-serif;font-weight:600;font-size:11px;line-height:16px;color:var(--white);text-align:center}
  .cover__quote::before{content:"\201C";position:absolute;left:-10px;top:-12px;font-size:22px}
  .cover__quote::after{content:"\201D";position:absolute;right:-6px;top:-12px;font-size:22px}

  /* Inside spread */
  .inside{left:415px;top:480px;width:710px;height:510px;background:var(--chalk);color:var(--white)}
  .inside__fold{position:absolute;left:355px;top:0;width:2px;height:100%;background:rgba(0,0,0,.35)}
  .stripes{position:absolute;left:0;top:0}
  .service{position:absolute;font-size:14px;font-weight:500;line-height:17px;letter-spacing:.3px;text-transform:uppercase}
  .service--tilt{transform:rotate(-18deg);transform-origin:left top}
  .inside .wordmark{color:var(--yellow);left:398px;top:42px;font-size:54px}
  .intro{position:absolute;left:430px;top:82px;width:265px;font-family:'Open Sans',sans-serif;font-weight:600;font-size:12px;line-height:17.5px}
  .intro span{display:block;text-indent:135px}
  .headline{position:absolute;left:405px;top:346px;width:280px;text-align:center;font-size:24px;font-weight:400;line-height:30px;text-transform:uppercase}
  .web{position:absolute;left:405px;top:411px;width:280px;text-align:center;font-family:'Open Sans',sans-serif;font-weight:600;font-size:12px}
</style>
</head>
<body>

<section class="spread cover">
  <div class="cover__band"></div>
  <div class="cover__fold"></div>

  <p class="wordmark wordmark--back">Drum</p>
  <address class="contact">
    Level 3, 42 Harbour Lane | Redfern | NSW, 2016<br>
    02 9471 3058 &nbsp;| &nbsp;info@drumpr.com.au
  </address>

  <p class="wordmark wordmark--front">Drum</p>
  <div class="cover__photo" role="img" aria-label="Photo of a young boy in oversized glasses and a tweed suit holding a book in front of a chalkboard"></div>
  <p class="cover__quote">CUSTOMER &amp; SHOPPER MARKET RESEARCH</p>
</section>

<section class="spread inside">
  <svg class="stripes" width="710" height="510" viewBox="0 0 710 545" preserveAspectRatio="none" aria-hidden="true">
    <g fill="var(--yellow)">
      <polygon points="0,82 128,94 128,100 0,90"/>
      <polygon points="290,148 392,133 392,140 290,155"/>
      <polygon points="22,276 140,214 143,221 25,283"/>
      <polygon points="300,240 440,247 440,255 300,248"/>
      <polygon points="25,304 170,297 170,304 25,311"/>
      <polygon points="268,352 352,322 354,329 270,359"/>
      <polygon points="358,320 436,300 438,307 360,327"/>
      <polygon points="40,426 185,420 185,427 40,433"/>
      <polygon points="298,443 352,428 354,435 300,450"/>
      <polygon points="358,427 392,417 394,424 360,434"/>
      <polygon points="442,360 695,328 696,337 443,369"/>
    </g>
  </svg>
  <div class="inside__fold"></div>

  <p class="service" style="left:132px;top:88px">New product<br>development</p>
  <p class="service" style="left:210px;top:138px;text-align:right">Product<br>testing</p>
  <p class="service service--tilt" style="left:142px;top:195px">Shopper<br>research</p>
  <p class="service" style="left:182px;top:220px;text-align:center">Customer<br>segmentation</p>
  <p class="service" style="left:176px;top:272px">Online<br>communities</p>
  <p class="service service--tilt" style="left:176px;top:344px">Customer<br>experience</p>
  <p class="service" style="left:193px;top:386px">Visualisation</p>
  <p class="service service--tilt" style="left:213px;top:440px">Bespoke<br>research</p>

  <p class="wordmark">Drum</p>
  <p class="intro"><span>is a progressive,</span>technology friendly market research agency, specialising in customer and shopper research. We help you connect with your customers so you can understand current behaviours, test new ideas, benchmark against your competition, plus a whole lot more. We do this by combining innovative methods, creative thinking, research expertise and a deep understanding of shopper and consumer decision-making.</p>

  <h2 class="headline">Understand your customer better</h2>
  <p class="web">find out more at www.drumpr.com.au</p>
</section>

</body>
</html>
```